Lively Ledgers - Minimalistic Single Page Web Design

Project: We are in the process of creating a new Corp Identity. Design a website for our company incorporating the Logo recently designed and selected from a ArtMarketo contest. (attached)

Designers: For this project, you need to design a minimalistic single page, modern website. Beside text and image placement, you will also need to describe user interface, how content is presented and so on.
- Design Layout
- Design Image placements (if any)
- Design menu and buttons
- Design menu and buttons placements
- Design content layout
- Design overall effect and feel of website
- Design color scheme
- Design content style (tone and style of content, words type, how much)
- Design user interface (how do you scroll, what happens when you mouseover buttons, where do certain links and buttons lead you)

Coding Requirements: You need to design the website with a modern perspective on website visuals and effects. Jquery, HTML5 (no FLASH please). You do not need to code for this particular contest, but if you can also code, great, tell me and let me know how I can hire you to complete it. If you know someone that can code your vision, great, let me know. If not, you need to be clear and concise, and be willing to help me communicate with a developer to get the site executed. The web site needs to be modern and dynamic.

Company Name:
Lively Ledgers; Lively-Ledgers; LivelyLedgers

Domain: www.lively-ledgers.com

Company Industry:
Lively Ledgers provides consulting in areas of finance, accounting, business organization, and set up.
- Bookkeeping
- Project Management
- Budget Management
- Cash Management
- Receipt Management
- Filing and Records Management
- Training of administration and accounting staff
- Financial Reports
- Spreadsheets
- Graphs, charts and trend analysis
- Business set up
- Tax filings
- Payroll and HR

Clients:
- Small to medium size businesses
- Proprietors
- Entrepreneurs
- Mom & Pops Shops
- We cater to every industry

Corporate Identity:
- Past: I have never complete a webpage for my company. I did scratch several projects that were started and never completed. I fell in love with stick figures, whimsical designs, similar to that of "Cloudvat", I believed in simplicity and minimalism. However, I was not effective in find the right people to complete my project. Bits and pieces of the website was designed, but never executed.

- Current: I need a webpage design. The web design must align with the current logo aesthetics.The current logo is new. I selected this logo for its simplicity and modern feel. It also incorporated an image of a trending graph, which fits with my company's profile. Still, I am leaning towards simple design, minimalism with boldness. I like my new webpage to be mature and professional, but I want it to portray energy and youth. So no "traditional corp" like design. I like new HTML5 elements, jquery and fun and beautiful forms and buttons. Less image is more.

Note: Please improvise according to your taste and professional perspective, you do not have to follow my suggestions word for word.

Features & Layout:
- Single page layout
- Vertical scroll
- Framed sections so that it looks good on the screen
- Well designed and strategically placed menu bar
- Fills a modern browser
- Beautiful color scheme that pops
- Incorporate Logo aesthetics

Fonts and Type:
- This is an element of the overall design
- I love clean fonts
- Fonts that adds meaning to the overall effect
- Clean

Sounds
- Please no cheesy sounds and background music

Images:
- To your liking
- But please, no lame corp people in suits
- No lame photographs
- I like stick figures
- I like whimsical illustrations

Landing Page:
- This should be the bulk of your design
- The landing page must be impressive, eye catchy
- Bold

Menu Bar:
- Header (introduction and landing page)
- Service & Products
- Company (about us)
- Affiliates and Clients (reference area)
- Contact (contact us area)
- Footer

Colors:
- Up to you, I just like things clean and easy to read
- No black background behind text
- Incorporate Logo Colors

Web Effects:
- According to your liking
- You will need to be involve to communicate the layout and design to the developer, so you need to be clear in your design.

Content:
- You personally don't have to come up with the content, but if you can great.
- I will help come up with the content throughout the contect timeframe, just let me know what you want
- I do not like too much content in my website. The most for each section is 2-3 lines if any.
- Combination could also be one liners.
- I like minimalistic approach.
- If you are not creating the final content, you need to show what type of content need to be created and in what style or tone.

Samples and Inspirations:
- http://singlesheetgallery.example/
- http://vantorix.example/#top
- http://brightmopservices.example/#about
- http://layoutjournal.example/inspiration/23-inspiring-single-page-designs
- http://www.kelvarstudio.example/
- http://www.dariuskessley.example/

This I do not want:
- Too much popups (none if possible)
- Images of people
- Images of people in suits
- Stereotypical images of accountants
- Scrolling marquee
- Clip arts
Updates

Designers, I want to stress the fact that I am looking for a design, not simply a website. The website is 1 page long. Text and content should be minimal. So this means that the design has to do most of the talking. Please do not submit template like web designs, I can pull this off myself if needed. I need you to design a great header, footer and the connecting tissue from landing to end of the page. The entire design needs to flow.

Again, please do not use images of corp people or anything like that. Please think outside the box in how you want to express the company.

Some ideas:
An illustration from beginning to end of the website, have a story.
Add colors to the back ground. 
The background should not get in the way of reading the text, but it does not have to be boring.
Be bold in your design.

Also, please describe more about your design when you submit. Please don't submit a template like design and have no explanation for your actions.

Also, fee free to ask me questions. I am here to help. I check this everyday, so please contact if you need anything.

Designers, please read the details of my post before you submit the design.

If you have a great concept idea but is worry, you can go ahead and submit a pencil draft and ask my opinion before you work anymore on it.

Please see the website samples below for what I am really looking for:

Reason: Hi everyone, I am extending the deadline. It looks like some design are still pending completion, and I want you to have enough time to work on it.

```html
<!DOCTYPE html>
<html lang="en">
<head>
<meta charset="utf-8">
<title>Lively Ledgers</title>
<link rel="stylesheet" href="https://fonts.googleapis.com/css2?family=Questrial&display=swap">
<style>
:root{
  --green:#8dc91f;
  --page-bg:#c8c8c8;
  --column:#ffffff;
  --rule:#6b6b6b;
  --text:#444444;
  --muted:#8a8a8a;
  --tab:#7a7a7a;
  --folder-back:#9a9a9a;
  --card:#959595;
  --footer:#575757;
}
*{box-sizing:border-box;margin:0;padding:0}
html,body{width:1200px;height:2880px;overflow:hidden}
body{background:var(--page-bg);font-family:"Questrial",sans-serif;color:var(--text);position:relative}
.column{position:absolute;left:132px;top:0;width:936px;height:2803px;background:var(--column)}
.abs{position:absolute}

/* header folder */
.folder-back{left:233px;top:96px;width:727px;height:451px;background:var(--folder-back);border-radius:28px;box-shadow:18px 22px 30px rgba(0,0,0,.45)}
.main-nav{left:0;top:115px;height:48px}
.main-nav a{position:absolute;top:0;height:48px;line-height:46px;text-align:center;font-size:21px;color:#fff;background:var(--tab);border-radius:14px 14px 0 0;text-decoration:none}
.main-nav a.active{background:#fff;color:var(--green)}
.folder-front{left:192px;top:158px;width:763px;height:370px;background:#fff;border-radius:44px 44px 36px 36px;box-shadow:0 4px 18px rgba(0,0,0,.35)}
.brand{left:192px;top:318px;width:763px;text-align:center;font-size:58px;color:var(--muted);letter-spacing:1px}

/* section headings: rules flex around the heading so they never cross it */
.section-title{left:132px;width:936px;height:60px;padding:0 53px;display:flex;align-items:center}
.section-title::before,.section-title::after{content:"";flex:1 1 0;height:5px;background:var(--rule)}
.section-title h2{flex:0 0 auto;margin:0 36px;font-weight:400;font-size:48px;line-height:60px;color:var(--green);white-space:nowrap}
.lead{left:132px;width:936px;text-align:center;font-size:21px;line-height:29px;color:var(--text)}

/* about word cloud & chart */
.chart{left:0;top:0;width:1200px;height:1200px}
.word{position:absolute;white-space:nowrap;font-size:26px;color:var(--muted)}
.word.key{font-size:37px;color:var(--green)}

/* service */
.service-art{left:192px;top:1356px;width:816px;height:252px;background:linear-gradient(90deg,#e8e8e8,#bfe07f 30%,#d6d6d6 55%,#a8d65a 80%,#e6e6e6);border-radius:126px}
.body-copy{font-size:20px;line-height:28px}

/* affiliates */
.card{top:1975px;height:257px;box-shadow:16px 18px 22px rgba(0,0,0,.4)}
.card.logo{background:var(--card);color:#adadad;text-align:center;padding-top:85px;font-size:26px;line-height:36px}
.card.logo strong{font-weight:400;font-size:34px}
.card.quote{background:var(--green);color:#fff;font-size:17px;line-height:22px;padding:14px 18px}
.card.quote .author{margin-top:24px}
.more{left:470px;top:2250px;width:260px;text-align:center;font-size:18px;color:var(--text);text-decoration:none}

/* contact */
.address{left:132px;top:2436px;width:936px;text-align:center;font-size:21px;line-height:26px;font-style:normal}
.address .phone{display:block;margin-top:6px}
.contact-form label{position:absolute;font-size:20px;color:var(--text)}
.field{position:absolute;background:#fff;border:1px solid #e3e3e3;box-shadow:4px 6px 8px rgba(0,0,0,.35)}
.submit{left:694px;top:2755px;font-size:19px;color:var(--text)}

.footer{left:0;top:2803px;width:1200px;height:77px;background:var(--footer);color:#fff;text-align:center;font-size:14px;line-height:17px;padding-top:14px}
</style>
</head>
<body>
<div class="column"></div>

<header>
  <div class="abs folder-back"></div>
  <nav class="abs main-nav">
    <a href="#about" style="left:247px;width:113px">about us</a>
    <a href="#service" class="active" style="left:377px;width:209px">service &amp; products</a>
    <a href="#affiliates" style="left:605px;width:197px">affiliates &amp; clients</a>
    <a href="#contact" style="left:816px;width:125px">contact us</a>
  </nav>
  <div class="abs folder-front"></div>
  <div class="abs brand">livelyledgers</div>
</header>

<section id="about">
  <div class="abs section-title" style="top:607px"><h2>about us</h2></div>
  <p class="abs lead" style="top:706px">Lively Ledgers provides consulting in areas of finance, accounting,<br>business organization, and set up.</p>

  <svg class="abs chart" viewBox="0 0 1200 1200" aria-hidden="true">
    <defs>
      <filter id="bar-shadow" x="-20%" y="-20%" width="160%" height="160%">
        <feDropShadow dx="14" dy="14" stdDeviation="9" flood-color="#000" flood-opacity=".4"/>
      </filter>
    </defs>
    <g fill="#8dc91f" filter="url(#bar-shadow)">
      <rect x="187" y="1099" width="79" height="65"/>
      <rect x="298" y="1123" width="77" height="41"/>
      <rect x="403" y="1099" width="79" height="65"/>
      <rect x="511" y="998" width="79" height="166"/>
      <rect x="617" y="989" width="79" height="175"/>
      <rect x="722" y="962" width="79" height="202"/>
      <rect x="830" y="890" width="79" height="274"/>
      <rect x="936" y="809" width="79" height="355"/>
    </g>
    <rect x="185" y="1174" width="830" height="5" fill="#6b6b6b" filter="url(#bar-shadow)"/>
  </svg>

  <span class="word key" style="left:185px;top:799px">Spreadsheets</span>
  <span class="word" style="left:461px;top:806px">Graphs, charts and trend analysis</span>
  <span class="word" style="left:185px;top:845px">Business set up</span>
  <span class="word" style="left:398px;top:845px">Budget Management</span>
  <span class="word key" style="left:679px;top:838px">Bookkeeping</span>
  <span class="word" style="left:185px;top:881px">Training of administration and accounting staff</span>
  <span class="word" style="left:185px;top:917px">Filing and Records Management</span>
  <span class="word key" style="left:617px;top:910px">Tax filings</span>
  <span class="word key" style="left:185px;top:946px">Payroll and HR</span>
  <span class="word" style="left:451px;top:953px">Cash Management</span>
  <span class="word" style="left:185px;top:987px">Project Management</span>
  <span class="word key" style="left:185px;top:1014px">Financial Reports</span>
  <span class="word" style="left:185px;top:1056px">Receipt Management</span>
</section>

<section id="service">
  <div class="abs section-title" style="top:1273px"><h2>service &amp; products</h2></div>
  <div class="abs service-art" role="img" aria-label="Two magnifying glasses, one over a green speech bubble and one over a green trend line"></div>
  <p class="abs lead body-copy" style="top:1644px">Lorem ipsum dolor sit amet, consectetur adipisicing elit, sed do eiusmod tempor<br>incididunt ut labore et dolore magna aliqua. Ut enim ad minim veniam, quis nostrud<br>exercitation ullamco laboris nisi ut aliquip ex ea commodo consequat.</p>
</section>

<section id="affiliates">
  <div class="abs section-title" style="top:1796px"><h2>affiliates &amp; clients</h2></div>
  <p class="abs lead" style="top:1882px">It is very easy to pride for ourselves, but our real pride<br>can be found on clients testimonials.</p>

  <div class="abs card logo" style="left:185px;width:257px">sample logo<br><strong>livelyledgers</strong></div>
  <div class="abs card logo" style="left:470px;width:260px">sample logo<br><strong>livelyledgers</strong></div>
  <blockquote class="abs card quote" style="left:758px;width:257px">
    <p>Lorem ipsum dolor sit amet, consectetur adipisicing elit, sed do eiusmod tempor incididunt ut labore et dolore magna aliqua. Ut enim ad minim veniam, quis nostrud exercitation ullamco laboris.</p>
    <p class="author">Evan Thorne<br>General Manager</p>
  </blockquote>

  <a class="abs more" href="#affiliates">read more testimonials</a>
  <svg class="abs" style="left:490px;top:2278px" width="220" height="26" viewBox="0 0 220 26" aria-hidden="true">
    <defs><linearGradient id="arrow-fade" x1="0" y1="0" x2="0" y2="1"><stop offset="0" stop-color="#9a9a9a"/><stop offset="1" stop-color="#e0e0e0"/></linearGradient></defs>
    <polygon points="0,0 220,0 110,26" fill="url(#arrow-fade)"/>
  </svg>
</section>

<section id="contact">
  <div class="abs section-title" style="top:2346px"><h2>contact us</h2></div>
  <address class="abs address">
    Lively Ledgers<br>xxxxxxxxxxxx street<br>xxxxxx City<br>State<br><span class="phone">telephone: xxxxxxxxxxxxxxx</span>
  </address>

  <form class="contact-form">
    <label style="left:448px;top:2598px">name</label>
    <span class="field" style="left:523px;top:2599px;width:233px;height:27px"></span>
    <label style="left:444px;top:2636px">e-mail</label>
    <span class="field" style="left:523px;top:2638px;width:233px;height:26px"></span>
    <span class="field" style="left:444px;top:2671px;width:312px;height:77px"></span>
    <span class="abs submit">submit</span>
    <svg class="abs" style="left:694px;top:2782px" width="60" height="12" viewBox="0 0 60 12" aria-hidden="true">
      <polygon points="0,0 60,0 30,12" fill="#cfcfcf"/>
    </svg>
  </form>
</section>

<footer class="abs footer">
  Copyright © 2013 Lively Ledgers<br>All Rights Reserved<br>Terms of Use
</footer>
</body>
</html>
```